Power Washing Business Easy Postcard Design

We need a postcard designed for our company, which does residential power washing. We clean houses, decks, driveways and fences. The design should be understated, high end with minimalist graphics. No bubbles or wild colors. The name of the business is "tallpine power washing" which should be rendered all lower case in a san serif font. Sample files in blue or white are attached. The attached files aren't our logo, just a model. The font doesn't have to be exact and "power washing" needs to be added to it.The postcard size is the Parcel Inkly 8.64" X 5.59". The photo which is attached should fill the whole front of the card.

The text elements on the front are:
1) "tallpine power washing"- as per the attached files, can be broken into two lines

2) "Mention this card and receive a FREE standard size Deck Wash"

3) "804-317-5286"

4) "tallpinepowerwashing.com" (this font size can be smaller than the phone number.)

5)"We Clean:- Houses- Decks- Driveways- Fences"The arrangement is the text is up to you. The text should not overpower the image.

Target Market(s)

Homeowners

Industry/Entity Type

Residential

Font styles to use
Sans Serif

Requirements
Should not have
• Garish graphics

```html
<!DOCTYPE html>
<html lang="en">
<head>
<meta charset="utf-8">
<title>tallpine power washing — postcard</title>
<link rel="stylesheet" href="https://fonts.googleapis.com/css2?family=Lato:wght@400;700;900&family=Libre+Baskerville:wght@400;700&display=swap">
<style>
  :root {
    --navy: #1e1f57;
    --red: #d8232a;
    --white: #ffffff;
    --paper: #f4f4f6;
    --band: #e4e4e8;
    --ink: #222230;
    --bg: #d9d9dc;
    --sky: #8fb3d9;
    --siding: #b7b4ae;
    --lawn: #4f7d2c;
  }
  * { margin: 0; padding: 0; box-sizing: border-box; }
  html, body { width: 800px; height: 1200px; overflow: hidden; }
  body { background: var(--bg); font-family: "Lato", sans-serif; position: relative; }

  .card { position: absolute; left: 67px; width: 666px; height: 516px; background: var(--paper); overflow: hidden; box-shadow: 0 4px 14px rgba(0,0,0,.25); }
  .card--front { top: 44px; background: linear-gradient(180deg, #fafafa 0%, var(--band) 100%); }
  .card--back { top: 616px; background: #fbfbfb; }

  .front-art { position: absolute; inset: 0; }

  .web-address { position: absolute; top: 22px; right: 20px; font-size: 14px; font-weight: 700; color: var(--navy); }

  .brand { position: absolute; text-align: left; color: var(--white); }
  .brand__name { font-family: "Libre Baskerville", serif; font-weight: 700; font-size: 32px; line-height: 1; letter-spacing: -.5px; }
  .brand__rule { height: 1px; background: currentColor; margin: 6px 0 4px; }
  .brand__tag { font-family: "Lato", sans-serif; font-size: 13.5px; letter-spacing: 1.2px; text-transform: uppercase; }
  .brand--front { left: 418px; top: 228px; }
  .brand--back { left: 39px; top: 52px; color: var(--navy); }
  .brand--back .brand__name { font-size: 24px; }
  .brand--back .brand__tag { font-size: 11px; }

  .services { position: absolute; left: 22px; top: 292px; width: 340px; text-align: center; color: var(--white); text-shadow: 0 1px 4px rgba(0,0,0,.7); }
  .services__title { font-family: "Libre Baskerville", serif; font-size: 24px; letter-spacing: .5px; text-transform: uppercase; }
  .services__list { margin-top: 6px; font-size: 17px; font-weight: 700; text-transform: uppercase; letter-spacing: .2px; }
  .services__dot { color: var(--red); margin: 0 3px; }
  .services__call { margin-top: 8px; font-size: 21px; font-weight: 900; display: flex; justify-content: center; align-items: center; gap: 6px; }
  .services__call-label { font-family: "Libre Baskerville", serif; font-size: 17px; color: var(--red); text-transform: uppercase; }

  .offer { position: absolute; left: 28px; right: 28px; top: 432px; text-align: center; color: var(--ink); }
  .offer__lead { font-size: 16px; font-weight: 700; letter-spacing: 11px; text-transform: uppercase; }
  .offer__rule { height: 2px; background: var(--ink); margin: 5px 0 6px; }
  .offer__main { font-family: "Libre Baskerville", serif; font-weight: 700; font-size: 27px; color: var(--navy); text-transform: uppercase; letter-spacing: -.5px; white-space: nowrap; }

  .back-photo { position: absolute; inset: 0; }
  .stamp-box { position: absolute; left: 532px; top: 52px; width: 90px; height: 109px; border: 1.5px solid var(--ink); }
  .address-line { position: absolute; left: 371px; width: 250px; height: 2px; background: var(--ink); }
</style>
</head>
<body>

<section class="card card--front">
  <svg class="front-art" viewBox="0 0 666 516" width="666" height="516">
    <defs>
      <linearGradient id="photoTones" x1="0" y1="0" x2="0" y2="1">
        <stop offset="0" stop-color="var(--sky)"/>
        <stop offset=".25" stop-color="#cdd6e2"/>
        <stop offset=".45" stop-color="var(--siding)"/>
        <stop offset=".68" stop-color="#8a857c"/>
        <stop offset=".8" stop-color="var(--lawn)"/>
        <stop offset="1" stop-color="#3c6421"/>
      </linearGradient>
    </defs>
    <path role="img" aria-label="Photograph of a large two-storey suburban house with lit windows, porch and green lawn at dusk"
          d="M0 0 H666 V220 C600 300 450 372 0 372 Z" fill="url(#photoTones)"/>
    <path d="M0 372 C450 372 600 300 666 220 V236 C600 318 450 388 0 388 Z" fill="var(--navy)"/>
    <path d="M0 388 C450 388 600 318 666 236 V258 C600 332 450 398 0 396 Z" fill="var(--red)"/>
    <circle cx="503" cy="249" r="112" fill="var(--navy)"/>
    <path d="M398 210 A112 112 0 0 1 540 142" fill="none" stroke="var(--white)" stroke-width="1.2" opacity=".7"/>
    <path d="M404 196 A118 118 0 0 1 560 140" fill="none" stroke="var(--white)" stroke-width="1" opacity=".5"/>
  </svg>

  <div class="web-address">www.tallpinepowerwashing.com</div>

  <div class="brand brand--front">
    <div class="brand__name">tallpine</div>
    <div class="brand__rule"></div>
    <div class="brand__tag">Power Washing</div>
  </div>

  <div class="services">
    <div class="services__title">We Clean</div>
    <div class="services__list"><span class="services__dot">•</span>Houses<span class="services__dot">•</span>Decks<span class="services__dot">•</span>Driveways<span class="services__dot">•</span>Fences</div>
    <div class="services__call">
      <svg width="16" height="16" viewBox="0 0 24 24" aria-hidden="true"><path fill="var(--red)" d="M6.6 10.8a15.1 15.1 0 0 0 6.6 6.6l2.2-2.2a1 1 0 0 1 1-.25 11.4 11.4 0 0 0 3.6.57 1 1 0 0 1 1 1V20a1 1 0 0 1-1 1A17 17 0 0 1 3 4a1 1 0 0 1 1-1h3.5a1 1 0 0 1 1 1c0 1.25.2 2.45.57 3.57a1 1 0 0 1-.25 1Z"/></svg>
      <span class="services__call-label">Call us</span>
      <span>804-317-5286</span>
    </div>
  </div>

  <div class="offer">
    <div class="offer__lead">Mention this card and receive</div>
    <div class="offer__rule"></div>
    <div class="offer__main">A free standard size deck wash</div>
  </div>
</section>

<section class="card card--back">
  <svg class="back-photo" viewBox="0 0 666 516" width="666" height="516">
    <defs>
      <linearGradient id="fadedTones" x1="0" y1="0" x2="0" y2="1">
        <stop offset="0" stop-color="#fbfbfb"/>
        <stop offset=".4" stop-color="#e6e6e8"/>
        <stop offset=".75" stop-color="#dcdcde"/>
        <stop offset="1" stop-color="#f0f0f1"/>
      </linearGradient>
    </defs>
    <rect role="img" aria-label="Faded light grey photograph of the same house as a background"
          x="0" y="60" width="666" height="456" fill="url(#fadedTones)"/>
  </svg>

  <div class="brand brand--back">
    <div class="brand__name">tallpine</div>
    <div class="brand__rule"></div>
    <div class="brand__tag">Power Washing</div>
  </div>

  <div class="stamp-box"></div>
  <div class="address-line" style="top:341px"></div>
  <div class="address-line" style="top:382px"></div>
  <div class="address-line" style="top:422px"></div>
</section>

</body>
</html>
```